Visitenkarten und Briefpapier für Beratungsunternehmen
Zielgruppe
Führungskräfte im Gesundheits- und Sozialwesen-
Aufgabenstellung
Wir suchen ein Set aus Briefpapier und Visitenkarten zu umserem Logo. Beides darf (muss nicht) beidseitig gestaltet werden.

```html
<!DOCTYPE html>
<html lang="de">
<head>
<meta charset="utf-8">
<title>Kelmarane – Briefpapier</title>
<link rel="stylesheet" href="https://fonts.googleapis.com/css2?family=Noto+Sans:wght@400&display=swap">
<style>
  :root {
    --brand-green: #5a9e2f;
    --brand-green-light: #a9d18a;
    --text: #1a1a1a;
    --footer-text: #555555;
    --paper: #ffffff;
  }
  html, body {
    margin: 0;
    padding: 0;
    overflow: hidden;
    background: var(--paper);
  }
  .letterhead {
    position: relative;
    width: 847px;
    height: 1200px;
    overflow: hidden;
    background: var(--paper);
    font-family: "Noto Sans", sans-serif;
    color: var(--text);
  }
  .side-band {
    position: absolute;
    left: 0;
    top: 112px;
    width: 19px;
    height: 1088px;
    background: var(--brand-green);
  }
  .top-rule {
    position: absolute;
    top: 0;
    left: 300px;
    width: 547px;
    height: 5px;
    background: linear-gradient(to right, rgba(90,158,47,0), var(--brand-green-light) 40%, var(--brand-green));
  }
  .brand {
    position: absolute;
    left: 62px;
    top: 108px;
    display: flex;
    align-items: center;
    gap: 10px;
  }
  .brand-dot {
    width: 14px;
    height: 14px;
    border-radius: 50%;
    background: var(--brand-green);
  }
  .brand-name {
    font-size: 30px;
    font-weight: 400;
    color: var(--text);
    line-height: 1;
  }
  .recipient {
    position: absolute;
    left: 109px;
    top: 266px;
    font-size: 13px;
    line-height: 17.5px;
    margin: 0;
    font-style: normal;
  }
  .letter-meta {
    position: absolute;
    left: 109px;
    top: 446px;
    width: 572px;
    display: flex;
    justify-content: space-between;
    font-size: 13px;
  }
  .letter-body {
    position: absolute;
    left: 109px;
    top: 476px;
    width: 572px;
    font-size: 12.4px;
    line-height: 18px;
  }
  .letter-body p {
    margin: 0 0 12px 0;
    text-align: justify;
  }
  .signature {
    position: absolute;
    left: 115px;
    top: 962px;
    font-size: 13px;
  }
  .footer-rule {
    position: absolute;
    right: 0;
    height: 3px;
    background: linear-gradient(to right, rgba(90,158,47,0), var(--brand-green-light) 30%, var(--brand-green));
  }
  .footer-rule.upper { top: 1176px; width: 700px; }
  .footer-rule.lower { top: 1188px; width: 520px; }
  .company-footer {
    position: absolute;
    left: 62px;
    top: 1084px;
    font-size: 11px;
    line-height: 23px;
    color: var(--footer-text);
    margin: 0;
  }
</style>
</head>
<body>
<main class="letterhead">
  <div class="side-band"></div>
  <div class="top-rule"></div>

  <header class="brand">
    <span class="brand-dot"></span>
    <span class="brand-name">Kelmarane</span>
  </header>

  <address class="recipient">
    Month 00, 200x<br>
    Addressee Name<br>
    Company Name<br>
    1234 Anywhere Avenue<br>
    Suite #0000<br>
    City, State 00000-0000<br>
    Country
  </address>

  <div class="letter-meta">
    <span class="salutation">Dear Addressee Name:</span>
    <span class="place-date">Ort, der 01.02.03</span>
  </div>

  <section class="letter-body">
    <p>Andipsum dipsum nostis nulpute magnissis niatie te molor adignis sequips uscipisit, sit vel ipsucing ent lut lan ulla feugait augueraesto odolore doluptatio cons dolor sismodo luptatuero do od dolore magnim dolor auguero eu facilis ea core estrud eugiat velis ad tat dio odolor augue magna corting eugait enim venibh et, quatumsan hendre tincinisi tisisl dolute moloreet atem velesequat alit aliquat, vel dolore faciduis dolore dignis dolorper il eugiamconsed deliquamcon henis alis atum duis at.</p>
    <p>Bore del ute faccum vercill aorper sent alit, venis autet, quipsustio eugue vero dolore velendre euis nos nonse dolessim illa feum dolor sumsan ectet lortincin vulputat amet, qui esto conulput acil in eugait vel essequam zzriusto diam, velit wissit autat.</p>
    <p>Obore dolor incip ea conummy nulput vel ullan henisim am in ute erciliqui ex ent et, quis augiat, commod tis enis num delit laor acing elis dolorer se eugue feu facinci liquis aut lut nulluptat er sum zzrit vulla consequis accum incidunt iusci blaortio odoloreet pratum veliquatie modit, quat. Ut nummodo exercilisl iriliqu ipsusto dolesequat. Ut wisl in ute consequam ad diam vulputpat lan hent vel doloreet utat ver si.</p>
    <p>Vullaorem iusci blamcon seniamcommy nit iureetum dolore con ea faccum iureet prat. In utat acidunt nullum venismolum ing exer iusci bla augue magna consequi ten veliquis nostion utpat.</p>
    <p>Do ea acilisis dolore min ercing endre consequat. Ero consequis ad euguerat, siscidunt laor sum iuscipis nullaoreet, velent ilit amconul laorperit lore diatum dui bla facipit irit alis ad dolorpe rostrud tem essequat praesequam, coreet ip er sim dit, velisim inciliquam, quis adigna feugue dolore et irillaor.</p>
    <p>Adiam zzrit,</p>
  </section>

  <div class="signature">Veliquatin Veraessi</div>

  <p class="company-footer">
    KELMARANE UG (Haftungsbeschränkt) | Lindenweg 14 | 54321 Musterstadt | Geschäftsführerin Hanna Berglind<br>
    Telefon 0123.45 67 89 | Fax 0123.45 67 90 | www.kelmaran.de | eMail info@kelmaran.de<br>
    St.-Nr. 00/000/0000/0 | Finanzamt Musterstadt | HRB-Nr. A 0000000<br>
    Musterbank Musterstadt eG | Konto 000 000 00 | BLZ 000 00 00 | IBAN DE00 000 0000 0000 0000 00 | SWIFT XXXXX 00000
  </p>

  <div class="footer-rule upper"></div>
  <div class="footer-rule lower"></div>
</main>
</body>
</html>
```